Celebration Cake brochure for boutique cake store

Looking for a cake brochure which displays the photo of the cake along with the description. Don't mind what style of brochure or size you do. We are a boutique bakery with both Italian and Australian cakes. I have a few ranges of products that I need to produce brochures (such as other sweets) but this is the first one required. *more photo to come

Industry/Entity Type

Bakery

Font styles to use
Sans Serif

Colors

Designer to choose colors to be used in the design.

Requirements
Must have
• Easy for customers to use the brochure to choose their cake. Don't mind what size brochure/menu you use

```html
<!DOCTYPE html>
<html lang="en">
<head>
<meta charset="utf-8">
<title>Vellucci's Pasticceria – Celebration Cakes Brochure</title>
<link href="https://fonts.googleapis.com/css2?family=Barlow:wght@300;400;500&display=swap" rel="stylesheet">
<style>
  :root {
    --backdrop: #2b2b2d;
    --ink-black: #111112;
    --sky-band: #a9cdee;
    --paper-grey: #e2e0da;
    --paper-cream: #efede1;
    --berry: #c9364f;
    --wine: #7a1f38;
    --white: #ffffff;
    --text-dark: #2a2a2a;
  }
  * { box-sizing: border-box; margin: 0; padding: 0; }
  html, body { width: 1200px; height: 789px; overflow: hidden; }
  body {
    background: var(--backdrop);
    font-family: "Barlow", sans-serif;
    display: flex;
    align-items: center;
    justify-content: center;
  }
  .spread { display: flex; width: 990px; height: 700px; }
  .panel { position: relative; width: 495px; height: 700px; overflow: hidden; }
  .panel-art { position: absolute; inset: 0; width: 100%; height: 100%; }

  /* back cover */
  .back-brand {
    position: absolute; left: 0; right: 0; top: 345px; text-align: center;
    color: var(--text-dark); font-weight: 400; font-size: 28px; line-height: 1.25;
  }
  .contact {
    position: absolute; left: 0; right: 0; top: 540px; text-align: center;
  }
  .contact-title { font-size: 15px; font-weight: 400; color: var(--text-dark); text-transform: uppercase; letter-spacing: .5px; }
  .contact-line { font-size: 19px; font-weight: 300; color: var(--wine); line-height: 1.3; }

  /* front cover */
  .front-brand {
    position: absolute; left: 0; right: 0; top: 80px; text-align: center;
    color: var(--white); font-weight: 400; font-size: 26px; line-height: 1.3;
  }
  .tagline {
    position: absolute; left: 45px; top: 330px;
    font-size: 22px; font-weight: 300; color: var(--text-dark); line-height: 1.25;
  }
  .cake-photo {
    position: absolute; left: 215px; top: 225px; width: 280px; height: 380px;
    background: radial-gradient(ellipse at 50% 45%, #6b4128 0%, #3e2414 55%, #2a180d 100%);
    border-radius: 48% 0 0 40%;
  }
  .web {
    position: absolute; left: 0; right: 0; bottom: 18px; text-align: center;
    color: var(--white); font-size: 16px; font-weight: 400; letter-spacing: .3px;
  }
</style>
</head>
<body>
  <main class="spread">
    <section class="panel back-cover">
      <svg class="panel-art" viewBox="0 0 495 700" preserveAspectRatio="none" aria-hidden="true">
        <rect width="495" height="700" fill="var(--paper-grey)"/>
        <path d="M0 0 H495 V230 Q250 250 0 345 Z" fill="var(--sky-band)"/>
        <path d="M0 0 H495 V195 Q250 215 0 305 Z" fill="var(--ink-black)"/>
      </svg>
      <p class="back-brand">Vellucci's<br>Pasticceria</p>
      <div class="contact">
        <p class="contact-title">Contact us</p>
        <p class="contact-line">(07) 3021-4856</p>
        <p class="contact-line">info@vellucci.com.au</p>
      </div>
    </section>

    <section class="panel front-cover">
      <svg class="panel-art" viewBox="0 0 495 700" preserveAspectRatio="none" aria-hidden="true">
        <rect width="495" height="700" fill="var(--paper-cream)"/>
        <path d="M0 0 H495 V220 Q300 225 0 300 Z" fill="var(--sky-band)"/>
        <path d="M0 0 H495 V188 Q300 195 0 270 Z" fill="var(--ink-black)"/>
        <path d="M0 640 Q250 632 495 600 V700 H0 Z" fill="var(--berry)"/>
      </svg>
      <p class="front-brand">Vellucci's<br>Pasticceria</p>
      <p class="tagline">Traditional,<br>Handmade<br>Italian Food,<br>Baked Locally<br>In Brisbane</p>
      <div class="cake-photo" role="img" aria-label="Photo of a chocolate celebration cake with shaved chocolate, cream rosettes and cherries on a gold board"></div>
      <p class="web">www.vellucci.com.au</p>
    </section>
  </main>
</body>
</html>
```